GPS Fleet Management web application design

We need an application UI design for a GPS fleet management application.
This is a WEB APPLICATION that will run in a desktop browser and not a mobile app design. Looking for a UI/UX expert with experience building desktop application designs.
UI needs to display map with real time location of fleet vehicles
Elements of the application would include things like reporting, geofencing, vehicle on-map displays, alerts, vehicle tabular listing with status (Online, offline, etc), vehicle detail info display like speed, engine rpm, etc etc.
You can blorvex vehicle tracking and get a sense of different GUIs. It is CRITICAL for the designer to understand fleet management applications to be able to do justice to the experience that we are trying to build and be successful in this project.
Looking for something different from the ordinary layout and with some GUI innovation. Should be simple to use, pleasant to look at with proper use of colors and very intuitive. We need a proper framework and user experience built and then on top of that we can add more panes and functionality as needed.
Some UX ideas include hiding things that are not required and resurfacing them easily on demand, being able to move panes around like a canvas, a comprehensive dashboard style layout on login and proper visualization of real time elements as they change.
Once we get some samples we will help the designer perfect it but we need to get some professional UI/UX person to conceptualize and design the user experience.
Reason: Added more time to be able to provide feedback
Gps

```html
<!DOCTYPE html>
<html lang="en">
<head>
<meta charset="utf-8">
<title>Fleet Dashboard</title>
<link rel="stylesheet" href="https://fonts.googleapis.com/css2?family=Roboto:wght@300;400;500;700&display=swap">
<style>
:root{
  --bar:#3e454f;
  --bar-field:#59616b;
  --side:#f4f5f7;
  --side-active:#e4e7eb;
  --main:#e9ebee;
  --card:#ffffff;
  --ink:#2f3540;
  --muted:#8a9099;
  --line:#e2e5e9;
  --green:#2fbf3a;
  --red:#e02424;
  --blue:#3b8fe0;
  --grey-dot:#c4c8cd;
  --map:#dde5ea;
  --sun:#f7c21b;
}
*{box-sizing:border-box;margin:0;padding:0}
html,body{width:1200px;height:884px;overflow:hidden;background:var(--main);font-family:"Roboto",sans-serif;color:var(--ink)}
.app{position:relative;width:1200px;height:884px}
.topbar{position:absolute;left:0;top:0;width:1200px;height:40px;background:var(--bar);display:flex;align-items:center}
.brand{width:232px;padding-left:14px;color:#fff;font-size:14px;font-weight:500}
.search{width:160px;height:22px;border-radius:11px;background:var(--bar-field);color:#aeb4bb;font-size:9px;display:flex;align-items:center;justify-content:space-between;padding:0 10px}
.bar-tools{margin-left:auto;display:flex;align-items:center;gap:22px;padding-right:18px}
.bell{position:relative}
.badge{position:absolute;top:-4px;right:-5px;width:8px;height:8px;border-radius:50%;background:var(--red)}
.me{width:26px;height:26px;border-radius:50%;background:#c9ccd1;border:2px solid #fff}
.sidebar{position:absolute;left:0;top:40px;width:232px;height:844px;background:var(--side);border-right:1px solid var(--line)}
.weather{height:70px;display:flex;align-items:center;padding:0 12px;gap:10px;background:#fff;border-bottom:1px solid var(--line)}
.temp{font-size:18px;font-weight:300;white-space:nowrap}
.temp small{font-size:10px;color:var(--muted);margin-left:4px}
.city,.date{font-size:9px;color:var(--muted)}
.clock{margin-left:auto;text-align:right;font-size:18px;font-weight:300}
.clock small{font-size:9px}
.side-title{height:36px;display:flex;align-items:center;padding-left:12px;font-size:11px;font-weight:500}
.driver{height:73.8px;display:flex;align-items:center;gap:8px;padding:0 8px;border-top:1px solid var(--line)}
.driver.active{background:var(--side-active)}
.avatar{width:28px;height:28px;border-radius:50%;background:linear-gradient(#b9a596,#7d6a5e);flex:none}
.driver-text{flex:1;min-width:0}
.driver-name{font-size:10.5px;font-weight:500;white-space:nowrap}
.driver-loc{font-size:8px;color:var(--muted);margin-top:3px;white-space:nowrap}
.dot{width:6px;height:6px;border-radius:50%;background:var(--green);flex:none}
.dot.off{background:var(--grey-dot)}
.subhead{position:absolute;left:232px;top:40px;width:968px;height:46px;padding:8px 14px;background:var(--side);border-bottom:1px solid var(--line)}
.subhead h1{font-size:11px;font-weight:500}
.subhead p{font-size:9px;color:var(--muted);margin-top:2px}
.status{position:absolute;right:14px;top:16px;font-size:9px;color:var(--green);font-weight:500}
.map{position:absolute;left:246px;top:96px;width:644px;height:384px;background:var(--map);overflow:hidden}
.pin{position:absolute;text-align:center}
.pin b{display:block;margin:0 auto 4px;width:24px;height:13px;border-radius:7px;background:var(--blue);color:#fff;font-size:8px;line-height:13px;font-weight:500}
.truck{width:32px;height:32px;border-radius:50%;background:#fff;border:2px solid var(--ink);display:flex;align-items:center;justify-content:center}
.halo{position:absolute;left:322px;top:147px;width:104px;height:104px;border-radius:50%;background:rgba(59,143,224,.18)}
.truck.alert{border-color:var(--red)}
.zoom{position:absolute;right:10px;top:232px;display:flex;flex-direction:column;gap:4px}
.zoom span{width:24px;height:24px;background:#fff;display:flex;align-items:center;justify-content:center;font-size:16px;color:var(--ink)}
.layer{position:absolute;right:8px;bottom:10px;width:48px;height:44px;background:#5d7d55}
.fleet{position:absolute;left:898px;top:96px;width:288px;height:384px;background:var(--card);padding:12px 16px;overflow:hidden}
.tabs{display:flex;height:30px;border:1px solid var(--line);margin-bottom:10px}
.tabs span{flex:1;display:flex;align-items:center;justify-content:center;font-size:10px;font-weight:500;color:var(--muted)}
.tabs .on{background:var(--bar);color:#fff}
.car{display:grid;grid-template-columns:86px 1fr;row-gap:6px;padding:10px 8px;font-size:9px;color:var(--muted);border-bottom:1px solid var(--line);height:55px;white-space:nowrap}
.car em{font-style:normal;color:var(--ink)}
.car.sel{border:1px solid #a9cdf2;background:#f5f9fe}
.panel{position:absolute;top:490px;height:380px;background:var(--card);padding:12px 10px;overflow:hidden}
.reporting{left:246px;width:350px}
.alerts{left:604px;width:350px}
.chart{left:962px;width:224px}
.panel h2{font-size:10px;font-weight:500;margin-bottom:10px}
.entry{display:flex;gap:10px;margin-bottom:18px}
.ico{width:22px;height:22px;border-radius:50%;background:#eef3fa;flex:none;display:flex;align-items:center;justify-content:center}
.alerts .ico{background:#fdeeee}
.entry p{font-size:8.5px;line-height:12px}
.entry time{display:block;font-size:7px;color:var(--muted);margin-top:2px}
.hot{color:var(--red)}
.legend{display:flex;justify-content:space-between;font-size:7px;color:var(--muted);position:absolute;left:10px;right:10px;bottom:14px}
.legend i{display:inline-block;width:8px;height:5px;margin-right:3px}
</style>
</head>
<body>
<div class="app">
  <header class="topbar">
    <div class="brand">Trakora</div>
    <div class="search">Search... <svg width="9" height="9" viewBox="0 0 10 10"><circle cx="4" cy="4" r="3" fill="none" stroke="#c8cdd2" stroke-width="1.3"/><path d="M6.3 6.3L9 9" stroke="#c8cdd2" stroke-width="1.3"/></svg></div>
    <div class="bar-tools">
      <span class="bell"><svg width="13" height="13" viewBox="0 0 14 14"><path d="M7 1a4 4 0 0 1 4 4v4l1.5 2h-11L3 9V5a4 4 0 0 1 4-4z M5.5 12h3a1.5 1.5 0 0 1-3 0z" fill="#fff"/></svg><span class="badge"></span></span>
      <svg width="13" height="13" viewBox="0 0 14 14" fill="none" stroke="#fff" stroke-width="1.5"><path d="M1 5V1h4M9 1h4v4M13 9v4H9M5 13H1V9"/></svg>
      <svg width="14" height="14" viewBox="0 0 14 14"><circle cx="7" cy="7" r="4.5" fill="none" stroke="#fff" stroke-width="2.5" stroke-dasharray="2.4 1.2"/><circle cx="7" cy="7" r="1.6" fill="#fff"/></svg>
      <span class="me" role="img" aria-label="User profile photo"></span>
    </div>
  </header>

  <aside class="sidebar">
    <div class="weather">
      <svg width="26" height="26" viewBox="0 0 26 26"><circle cx="13" cy="13" r="6" fill="var(--sun)"/><g stroke="var(--sun)" stroke-width="2"><path d="M13 1v4M13 21v4M1 13h4M21 13h4M4.5 4.5l2.8 2.8M18.7 18.7l2.8 2.8M4.5 21.5l2.8-2.8M18.7 7.3l2.8-2.8"/></g></svg>
      <div><div class="temp">28°C<small>| sunny</small></div><div class="city">London</div></div>
      <div class="clock">9:43<small>AM</small><div class="date">16-Oct-2017</div></div>
    </div>
    <div class="side-title">Lorem Ipsum Dolor</div>
    <div class="driver"><span class="avatar" role="img" aria-label="Driver photo"></span><div class="driver-text"><div class="driver-name">Eadric Watson</div><div class="driver-loc">Location: Lorem ipsum dolor sit amet St.</div></div><span class="dot"></span></div>
    <div class="driver"><span class="avatar" role="img" aria-label="Driver photo"></span><div class="driver-text"><div class="driver-name">Addison Smith</div><div class="driver-loc">Location: Lorem ipsum dolor sit amet St.</div></div><span class="dot"></span></div>
    <div class="driver"><span class="avatar" role="img" aria-label="Driver photo"></span><div class="driver-text"><div class="driver-name">Rafael O neill</div><div class="driver-loc">Location: Lorem ipsum dolor sit amet St.</div></div><span class="dot off"></span></div>
    <div class="driver active"><span class="avatar" role="img" aria-label="Driver photo"></span><div class="driver-text"><div class="driver-name">Jack Miller</div><div class="driver-loc">Location: Lorem ipsum dolor sit amet St.</div></div><span class="dot"></span></div>
    <div class="driver"><span class="avatar" role="img" aria-label="Driver photo"></span><div class="driver-text"><div class="driver-name">Paavo Collins</div><div class="driver-loc">Location: Lorem ipsum dolor sit amet St.</div></div><span class="dot"></span></div>
    <div class="driver"><span class="avatar" role="img" aria-label="Driver photo"></span><div class="driver-text"><div class="driver-name">Adlof Thomas</div><div class="driver-loc">Location: Lorem ipsum dolor sit amet St.</div></div><span class="dot"></span></div>
    <div class="driver"><span class="avatar" role="img" aria-label="Driver photo"></span><div class="driver-text"><div class="driver-name">Fang Richards</div><div class="driver-loc">Location: Lorem ipsum dolor sit amet St.</div></div><span class="dot off"></span></div>
    <div class="driver"><span class="avatar" role="img" aria-label="Driver photo"></span><div class="driver-text"><div class="driver-name">Macario Brooks</div><div class="driver-loc">Location: Lorem ipsum dolor sit amet St.</div></div><span class="dot off"></span></div>
    <div class="driver"><span class="avatar" role="img" aria-label="Driver photo"></span><div class="driver-text"><div class="driver-name">Gael Scott</div><div class="driver-loc">Location: Lorem ipsum dolor sit amet St.</div></div><span class="dot"></span></div>
    <div class="driver"><span class="avatar" role="img" aria-label="Driver photo"></span><div class="driver-text"><div class="driver-name">Aldwin Wells</div><div class="driver-loc">Location: Lorem ipsum dolor sit amet St.</div></div><span class="dot"></span></div>
  </aside>

  <section class="subhead">
    <h1>Jack Miller</h1>
    <p>Lorem ipsum dolor sit amet, consectetur adipiscing elit.</p>
    <span class="status">ONLINE</span>
  </section>

  <section class="map" role="img" aria-label="City street map showing live vehicle positions">
    <div class="halo"></div>
    <div class="pin" style="left:130px;top:30px"><b>A1</b><div class="truck"><svg width="16" height="12" viewBox="0 0 16 12"><path d="M1 1h9v8H1zM10 4h3l2 3v2h-5z" fill="var(--ink)"/><circle cx="4" cy="10" r="1.6" fill="var(--ink)"/><circle cx="12" cy="10" r="1.6" fill="var(--ink)"/></svg></div></div>
    <div class="pin" style="left:578px;top:92px"><b>A6</b><div class="truck"><svg width="16" height="12" viewBox="0 0 16 12"><path d="M1 1h9v8H1zM10 4h3l2 3v2h-5z" fill="var(--ink)"/><circle cx="4" cy="10" r="1.6" fill="var(--ink)"/><circle cx="12" cy="10" r="1.6" fill="var(--ink)"/></svg></div></div>
    <div class="pin" style="left:358px;top:170px"><b>A4</b><div class="truck alert"><svg width="16" height="12" viewBox="0 0 16 12"><path d="M1 1h9v8H1zM10 4h3l2 3v2h-5z" fill="var(--red)"/><circle cx="4" cy="10" r="1.6" fill="var(--red)"/><circle cx="12" cy="10" r="1.6" fill="var(--red)"/></svg></div></div>
    <div class="pin" style="left:18px;top:210px"><b>A2</b><div class="truck"><svg width="16" height="12" viewBox="0 0 16 12"><path d="M1 1h9v8H1zM10 4h3l2 3v2h-5z" fill="var(--ink)"/><circle cx="4" cy="10" r="1.6" fill="var(--ink)"/><circle cx="12" cy="10" r="1.6" fill="var(--ink)"/></svg></div></div>
    <div class="pin" style="left:238px;top:240px"><b>A3</b><div class="truck"><svg width="16" height="12" viewBox="0 0 16 12"><path d="M1 1h9v8H1zM10 4h3l2 3v2h-5z" fill="var(--ink)"/><circle cx="4" cy="10" r="1.6" fill="var(--ink)"/><circle cx="12" cy="10" r="1.6" fill="var(--ink)"/></svg></div></div>
    <div class="pin" style="left:458px;top:265px"><b>A5</b><div class="truck"><svg width="16" height="12" viewBox="0 0 16 12"><path d="M1 1h9v8H1zM10 4h3l2 3v2h-5z" fill="var(--ink)"/><circle cx="4" cy="10" r="1.6" fill="var(--ink)"/><circle cx="12" cy="10" r="1.6" fill="var(--ink)"/></svg></div></div>
    <div class="zoom"><span><svg width="12" height="12" viewBox="0 0 12 12"><circle cx="6" cy="6" r="4" fill="none" stroke="var(--ink)" stroke-width="1.3"/><circle cx="6" cy="6" r="1.5" fill="var(--ink)"/></svg></span><span>+</span><span>−</span></div>
    <div class="layer" role="img" aria-label="Satellite view toggle"></div>
  </section>

  <section class="fleet">
    <div class="tabs"><span class="on">ONLINE</span><span>OFFLINE</span></div>
    <div class="car"><span>Car: <em>A1</em></span><span>Location: <em>Lorem Ipsum Highway St.</em></span><span>Miles: <em>30</em></span><span>Speed: <em>62 mph</em></span></div>
    <div class="car"><span>Car: <em>A2</em></span><span>Location: <em>Lorem Ipsum Highway St.</em></span><span>Miles: <em>32</em></span><span>Speed: <em>53 mph</em></span></div>
    <div class="car"><span>Car: <em>A3</em></span><span>Location: <em>Lorem Ipsum Highway St.</em></span><span>Miles: <em>28</em></span><span>Speed: <em>58 mph</em></span></div>
    <div class="car sel"><span>Car: <em>A4</em></span><span>Location: <em>Lorem Ipsum Highway St.</em></span><span>Miles: <em>37</em></span><span>Speed: <em>65 mph</em></span></div>
    <div class="car"><span>Car: <em>A5</em></span><span>Location: <em>Lorem Ipsum Highway St.</em></span><span>Miles: <em>41</em></span><span>Speed: <em>70 mph</em></span></div>
    <div class="car"><span>Car: <em>A6</em></span><span>Location: <em>Lorem Ipsum Highway St.</em></span><span>Miles: <em>42</em></span><span>Speed: <em>60 mph</em></span></div>
  </section>

  <section class="panel reporting">
    <h2>Reporting</h2>
    <div class="entry"><span class="ico"><svg width="11" height="10" viewBox="0 0 11 10"><path d="M1 3h3l5-2.5v9L4 7H1z" fill="var(--blue)"/></svg></span><p>Lorem ipsum dolor sit amet, consectetur adipiscing elit. Etiam vitae eros efficitur, finibus sapien et, porta libero. Integer facilisis massa dolor.<time>16-Oct-2017 9:15 AM</time></p></div>
    <div class="entry"><span class="ico"><svg width="11" height="10" viewBox="0 0 11 10"><path d="M1 3h3l5-2.5v9L4 7H1z" fill="var(--blue)"/></svg></span><p>Lorem ipsum dolor sit amet, consectetur adipiscing elit. Etiam vitae eros efficitur, finibus sapien et, porta libero. Integer facilisis massa dolor.<time>16-Oct-2017 9:15 AM</time></p></div>
    <div class="entry"><span class="ico"><svg width="11" height="10" viewBox="0 0 11 10"><path d="M1 3h3l5-2.5v9L4 7H1z" fill="var(--blue)"/></svg></span><p>Lorem ipsum dolor sit amet, consectetur adipiscing elit. Etiam vitae eros efficitur, finibus sapien et, porta libero. Integer facilisis massa dolor.<time>16-Oct-2017 9:15 AM</time></p></div>
    <div class="entry"><span class="ico"><svg width="11" height="10" viewBox="0 0 11 10"><path d="M1 3h3l5-2.5v9L4 7H1z" fill="var(--blue)"/></svg></span><p>Lorem ipsum dolor sit amet, consectetur adipiscing elit. Etiam vitae eros efficitur, finibus sapien et, porta libero. Integer facilisis massa dolor.<time>16-Oct-2017 9:15 AM</time></p></div>
    <div class="entry"><span class="ico"><svg width="11" height="10" viewBox="0 0 11 10"><path d="M1 3h3l5-2.5v9L4 7H1z" fill="var(--blue)"/></svg></span><p>Lorem ipsum dolor sit amet, consectetur adipiscing elit. Etiam vitae eros efficitur, finibus sapien et, porta libero. Integer facilisis massa dolor.<time>16-Oct-2017 9:15 AM</time></p></div>
  </section>

  <section class="panel alerts">
    <h2>Alerts</h2>
    <div class="entry"><span class="ico"><svg width="11" height="10" viewBox="0 0 11 10"><path d="M5.5 0L11 10H0z" fill="var(--red)"/></svg></span><p>Lorem ipsum dolor sit amet, <span class="hot">consectetur adipiscing elit.</span> Etiam vitae eros efficitur, finibus sapien et, porta libero. Integer facilisis massa dolor.<time>16-Oct-2017 9:15 AM</time></p></div>
    <div class="entry"><span class="ico"><svg width="11" height="10" viewBox="0 0 11 10"><path d="M5.5 0L11 10H0z" fill="var(--red)"/></svg></span><p>Lorem <span class="hot">ipsum dolor sit amet, consectetur</span> adipiscing elit. Etiam vitae eros efficitur, finibus sapien et, porta libero. Integer facilisis <span class="hot">massa dolor.</span><time>16-Oct-2017 9:15 AM</time></p></div>
    <div class="entry"><span class="ico"><svg width="11" height="10" viewBox="0 0 11 10"><path d="M5.5 0L11 10H0z" fill="var(--red)"/></svg></span><p>Lorem ipsum dolor sit amet, consectetur adipiscing elit. Etiam vitae eros efficitur, finibus sapien <span class="hot">et, porta libero.</span> Integer facilisis massa dolor.<time>16-Oct-2017 9:15 AM</time></p></div>
    <div class="entry"><span class="ico"><svg width="11" height="10" viewBox="0 0 11 10"><path d="M5.5 0L11 10H0z" fill="var(--red)"/></svg></span><p>Lorem ipsum dolor sit amet, consectetur adipiscing elit. <span class="hot">Etiam vitae eros efficitur,</span> finibus sapien et, porta libero. Integer facilisis massa dolor.<time>16-Oct-2017 9:15 AM</time></p></div>
    <div class="entry"><span class="ico"><svg width="11" height="10" viewBox="0 0 11 10"><path d="M5.5 0L11 10H0z" fill="var(--red)"/></svg></span><p>Lorem ipsum dolor sit amet, consectetur adipiscing elit. Etiam vitae eros efficitur, finibus sapien et, porta libero. Integer facilisis massa dolor.<time>16-Oct-2017 9:15 AM</time></p></div>
  </section>

  <section class="panel chart">
    <svg width="204" height="300" viewBox="-102 -150 204 300">
      <g transform="translate(0,-30) scale(1.35)">
        <path d="M0 0L0 -60A60 60 0 0 1 40.9 -43.9Z" fill="var(--red)"/>
        <path d="M0 0L40.9 -43.9A60 60 0 0 1 -20.5 56.4Z" fill="var(--green)"/>
        <path d="M0 0L-20.5 56.4A60 60 0 0 1 0 -60Z" fill="#e4e4e4"/>
      </g>
    </svg>
    <div class="legend"><span><i style="background:var(--red)"></i>Lorem ipsum</span><span><i style="background:var(--green)"></i>Lorem ipsum</span><span><i style="background:#e4e4e4"></i>Lorem ipsum</span></div>
  </section>
</div>
</body>
</html>
```